Recruitment of Philippine Manpower for the UK market

I want a website for the UK market to attract businesses and companies to come to us for Philipine labour. We want an information site that gives all information on what we do and how we can recruit Philippine labour.
This is a recruitment site for companies to contact us with their requirements for skilled workers coming from the Philipines over to the UK to work.

Target Market(s)

Uk Companies and businesses who want Philipine skilled workers

Industry/Entity Type

REcruitment

Coding

Coded - Design and coding required

Number of Pages Required

5+ page

Font styles to use
Sans Serif

Colors
0054AA
0677BA
7BADD7
CADEEF
E8F1F8
0094D4
00A9DD
6FCCEA
C7EBF8
E9F6FB
EE7325
F08F49
F5BC92
FAE3D3
FDF4ED
EB3D1F
EC4F4E
F09395
F8D3D4
FCEDEE

Requirements
Must have
• Look professional and corperate with drop down menus for Home ,about, services,articles. training , contact us
Nice to have
• Look at Tovel recruitment- https://tovelrecruitment.example.co.uk/. This is my current site - https://www.brindlestaffing.example.com/
Should not have
• Cartoons or silly pictures , needs to be corperate looking

```html
<!DOCTYPE html>
<html lang="en">
<head>
<meta charset="utf-8">
<title>Brindle Staffing – Skilled Philippine Workers for UK Companies</title>
<link href="https://fonts.googleapis.com/css2?family=Audiowide&family=Poppins:wght@400;500;600;700&display=swap" rel="stylesheet">
<style>
:root{
  --red:#d3112a;
  --red-dark:#b50d22;
  --yellow:#fdd216;
  --ink:#111111;
  --grey-text:#444444;
  --pink-band:#f6e6e8;
  --faint:#ececec;
  --footer:#000000;
  --map:#a9a9a9;
  --white:#ffffff;
}
*{box-sizing:border-box;margin:0;padding:0}
html,body{width:1200px;height:4777px;overflow:hidden;background:var(--white)}
body{font-family:"Poppins",sans-serif;color:var(--ink)}
.page{position:relative;width:1200px;height:4777px;overflow:hidden}
.abs{position:absolute}
.display{font-family:"Audiowide",sans-serif;text-transform:uppercase;line-height:1}

/* header */
.brand{left:89px;top:40px;display:flex;align-items:center;gap:12px}
.brand-mark{width:34px;height:34px;border-radius:50%;background:var(--red)}
.brand-name{font-family:"Poppins",sans-serif;font-weight:700;font-size:20px;text-transform:uppercase;color:var(--ink);letter-spacing:.5px}
.nav{left:556px;top:36px;display:flex;align-items:center;gap:26px;font-weight:600;font-size:13px}
.nav a{color:var(--ink);text-decoration:none}
.btn-contact{left:980px;top:24px;width:129px;height:46px;border:2px solid var(--red);color:var(--red);font-weight:600;font-size:12px;display:flex;align-items:center;justify-content:center;text-decoration:none}

/* hero */
.pink-band{left:425px;top:0;width:167px;height:440px;background:var(--pink-band)}
.hero-title{left:0;top:228px;width:1200px;text-align:center;font-size:42px;letter-spacing:1px}
.hero-title span{display:block;margin-bottom:5px}
.hero-title .accent{color:var(--red)}
.ghost-word{left:10px;top:450px;width:1180px;text-align:center;font-size:178px;color:var(--faint);letter-spacing:6px}
.hero-photo{left:278px;top:371px;width:659px;height:547px;border-radius:40% 40% 8px 8px;background:linear-gradient(180deg,#e9eef3 0%,#c9d7e6 40%,#8aa0b8 100%)}
.stats{left:976px;top:672px}
.stat{margin-bottom:38px}
.stat b{display:block;font-family:"Audiowide",sans-serif;font-size:24px;line-height:1}
.stat small{font-size:15px;color:var(--grey-text)}

/* about */
.about-title{left:158px;top:1070px;font-size:42px;line-height:1.12}
.about-text{left:158px;top:1220px;width:495px;font-size:15px;line-height:27px;color:var(--grey-text)}
.photo-stack{left:649px;top:946px;width:423px;height:501px}
.stack-sheet{position:absolute;background:var(--white);box-shadow:0 6px 22px rgba(0,0,0,.15)}
.stack-sheet.a{left:20px;top:40px;width:350px;height:430px;transform:rotate(-8deg)}
.stack-sheet.b{left:50px;top:20px;width:350px;height:430px;transform:rotate(6deg)}
.stack-sheet.c{left:52px;top:18px;width:335px;height:470px;padding:20px 16px}
.stack-photo{width:100%;height:100%;background:linear-gradient(160deg,#9aa7b3 0%,#c7a778 45%,#6f7f90 100%)}

/* services */
.tile{top:1503px;width:214px;height:231px;color:var(--white);padding:0 28px 28px}
.tile.red{background:var(--red)}
.tile.yellow{background:var(--yellow);color:var(--ink)}
.tile svg{position:absolute;left:30px;top:40px}
.tile .label{position:absolute;left:30px;bottom:30px;font-size:16px;line-height:1.05}
.btn-outline{left:523px;top:1757px;width:154px;height:46px;border:2px solid var(--ink);font-weight:600;font-size:12px;display:flex;align-items:center;justify-content:center}

/* training */
.training{left:0;top:1887px;width:1200px;height:538px;background:linear-gradient(110deg,#6b4a2a 0%,#c98a3c 35%,#e7d2a8 55%,#b7bf7a 70%,#e06a2a 100%)}
.training-word{left:89px;top:2330px;font-size:98px;color:var(--white);letter-spacing:2px}
.play{left:1013px;top:2349px;width:96px;height:96px;border-radius:50%;background:var(--yellow);box-shadow:0 0 0 10px rgba(253,210,22,.3)}
.play svg{position:absolute;left:36px;top:30px}

/* working together */
.wt-title{left:158px;top:2594px;font-size:44px}
.wt-sub{left:158px;top:2652px;font-size:27px;line-height:31px}
.red-band{left:0;top:2953px;width:1200px;height:321px;background:linear-gradient(180deg,var(--red) 0%,var(--red-dark) 100%)}
.card{top:2758px;width:214px;height:232px;background:var(--white);box-shadow:0 6px 20px rgba(0,0,0,.1);padding:0 20px}
.card svg{position:absolute;left:22px;top:24px}
.card .num{position:absolute;right:18px;top:30px;font-family:"Audiowide",sans-serif;font-size:34px;color:#e4e4e4}
.card h3{position:absolute;left:20px;top:118px;font-family:"Audiowide",sans-serif;font-weight:400;font-size:15px}
.card p{position:absolute;left:20px;top:146px;width:178px;font-size:11.5px;line-height:17px;color:var(--grey-text)}
.band-link{top:3120px;font-size:23px;color:var(--white);line-height:1.15}
.band-arrow{top:3126px}

/* blog */
.blog-title{left:158px;top:3502px;font-size:42px;line-height:1.12}
.see-all{left:158px;top:3652px;font-weight:700;font-size:15px;color:var(--red);display:flex;align-items:center;gap:14px}
.post{top:3376px;width:307px;height:399px;background:var(--white);box-shadow:0 6px 20px rgba(0,0,0,.1)}
.post-photo{height:254px}
.post h4{margin:36px 28px 0;font-family:"Audiowide",sans-serif;font-weight:400;font-size:18px;line-height:22px}
.post .more{margin:6px 28px 0;font-weight:700;font-size:14px;color:var(--red)}

/* map + footer */
.footer{left:0;top:4304px;width:1200px;height:473px;background:var(--footer)}
.map{left:160px;top:3881px;width:881px;height:475px;background:var(--map)}
.f-brand{left:167px;top:4520px;display:flex;align-items:center;gap:12px}
.f-brand .brand-name{color:var(--white);font-size:21px}
.f-contact-title{left:508px;top:4478px;font-size:24px;color:var(--white)}
.f-lines{left:508px;top:4518px;color:var(--white);font-size:15px;line-height:27px}
.f-lines div{display:flex;align-items:flex-start;gap:12px}
.f-lines svg{margin-top:7px;flex:none}
.social{top:4534px;width:32px;height:32px;border-radius:50%}
.rule{left:89px;top:4712px;width:1022px;height:1px;background:#333}
.copy{left:0;top:4736px;width:1200px;text-align:center;color:var(--white);font-size:15px}
.to-top{left:1123px;top:4692px;width:40px;height:40px;border-radius:50%;background:var(--red)}
.to-top svg{position:absolute;left:14px;top:15px}
</style>
</head>
<body>
<div class="page">

  <!-- header -->
  <div class="abs pink-band"></div>
  <div class="abs brand"><span class="brand-mark"></span><span class="brand-name">Brindle Staffing</span></div>
  <nav class="abs nav">
    <svg width="14" height="13" viewBox="0 0 14 13"><path d="M7 0 L14 6 H12 V13 H8.5 V9 H5.5 V13 H2 V6 H0 Z" fill="#fdd216"/></svg>
    <a href="#">ABOUT</a><a href="#">SERVICES</a><a href="#">ARTICLES</a><a href="#">TRAINING</a>
  </nav>
  <a class="abs btn-contact" href="#">CONTACT US</a>

  <!-- hero -->
  <div class="abs display ghost-word">WORKERS</div>
  <h1 class="abs display hero-title">
    <span class="accent">Recruiting and Placing</span>
    <span>Skilled Philippine Workers</span>
    <span>Into UK Companies</span>
  </h1>
  <div class="abs hero-photo" role="img" aria-label="Group of skilled workers in uniforms: chefs, office staff, mechanic and construction workers"></div>
  <div class="abs stats">
    <div class="stat"><b>5500+</b><small>People Recruited</small></div>
    <div class="stat"><b>100+</b><small>Happy Clients</small></div>
    <div class="stat"><b>10+</b><small>Countries</small></div>
  </div>

  <!-- about -->
  <h2 class="abs display about-title">What the<br>business is<br>about</h2>
  <p class="abs about-text">We source skilled workers directly from the Philippines to work in the UK. With offices , training locations and specialist recruiters we can find the highest quality individuals to add value and resources to any UK buisness. We delivery quality based on vast experience over a number of years.</p>
  <div class="abs photo-stack">
    <div class="stack-sheet a"></div>
    <div class="stack-sheet b"></div>
    <div class="stack-sheet c"><div class="stack-photo" role="img" aria-label="Three construction workers in hi-vis vests and tool belts on site"></div></div>
  </div>

  <!-- services -->
  <div class="abs tile red" style="left:161px">
    <svg width="74" height="74" viewBox="0 0 74 74" fill="none" stroke="#fff" stroke-width="2.5"><circle cx="37" cy="37" r="34"/><path d="M37 58 V32 M37 40 C28 40 24 34 24 28 C31 28 37 32 37 40 M37 36 C46 36 50 30 50 24 C43 24 37 28 37 36 M14 54 H60"/></svg>
    <div class="label display">Agriculture</div>
  </div>
  <div class="abs tile yellow" style="left:382px">
    <svg width="74" height="74" viewBox="0 0 74 74" fill="none" stroke="#111" stroke-width="2.5"><path d="M6 72 H70 M14 72 V44 H34 V72 M18 44 V30 H30 V44 M20 30 V18 H28 V30 M12 12 H36 M44 72 V50 L48 44 V36 H52 V44 L56 50 V72 M58 72 V54 L62 50 V42 H66 V50 L70 54 V72"/></svg>
    <div class="label display">Food<br>Processing</div>
  </div>
  <div class="abs tile red" style="left:605px">
    <svg width="78" height="74" viewBox="0 0 78 74" fill="none" stroke="#fff" stroke-width="2.5"><path d="M33 10 H45 M39 10 V18 M6 50 C6 30 22 18 39 18 C56 18 72 30 72 50 Z M2 56 H76 M20 62 H58 L52 70 H26 Z"/></svg>
    <div class="label display">Hospitality<br>and Catering</div>
  </div>
  <div class="abs tile red" style="left:825px">
    <svg width="78" height="74" viewBox="0 0 78 74" fill="none" stroke="#fff" stroke-width="2.5"><path d="M4 72 H74 M10 72 V40 L24 30 L38 40 V72 M16 72 V56 H32 V72 M46 72 V16 H56 V72 M30 16 H76 M46 16 L56 4 L56 16 M70 16 V30 M66 30 H74 V36 H66 Z"/></svg>
    <div class="label display">Building and<br>Construction</div>
  </div>
  <div class="abs btn-outline">VIEW SERVICES</div>

  <!-- training -->
  <div class="abs training" role="img" aria-label="Smiling construction team in hard hats and hi-vis vests reviewing site plans"></div>
  <div class="abs display training-word">Training</div>
  <div class="abs play"><svg width="30" height="36" viewBox="0 0 30 36"><path d="M0 0 L30 18 L0 36 Z" fill="#fff"/></svg></div>

  <!-- working together -->
  <h2 class="abs display wt-title">Working Together</h2>
  <p class="abs display wt-sub">We recruit the finest talent available with<br>our dedicated 200 strong team</p>
  <div class="abs red-band"></div>

  <div class="abs card" style="left:161px">
    <svg width="72" height="56" viewBox="0 0 72 56" fill="none" stroke="#d3112a" stroke-width="2"><rect x="2" y="10" width="52" height="34"/><path d="M18 52 H38 M28 44 V52"/><circle cx="54" cy="12" r="8"/><circle cx="54" cy="12" r="3"/></svg>
    <span class="num">01</span>
    <h3>WHAT WE DO</h3>
    <p>Our company has been established in the Philippines for over 20 years...</p>
  </div>
  <div class="abs card" style="left:382px">
    <svg width="62" height="58" viewBox="0 0 62 58" fill="none" stroke="#d3112a" stroke-width="2"><path d="M4 56 L20 30 L32 40 L44 30 L58 56 M20 30 L30 8 M44 30 L34 8 M24 36 L38 22"/></svg>
    <span class="num">02</span>
    <h3>HOW WE HELP</h3>
    <p>We work with companies to find skilled workers that meet the UK requirements..</p>
  </div>
  <div class="abs card" style="left:605px">
    <svg width="60" height="60" viewBox="0 0 60 60" fill="none" stroke="#d3112a" stroke-width="2"><path d="M56 4 C38 4 24 14 18 32 L28 42 C46 36 56 22 56 4 Z M18 32 L8 30 L16 20 H26 M28 42 L30 52 L40 44 V34 M14 46 L4 56"/><circle cx="40" cy="20" r="5"/></svg>
    <span class="num">03</span>
    <h3>WHERE TO START</h3>
    <p>We need to know what your issues are and how we can understand the personnal..</p>
  </div>
  <div class="abs card" style="left:825px">
    <svg width="66" height="56" viewBox="0 0 66 56" fill="none" stroke="#d3112a" stroke-width="2"><path d="M8 6 L16 4 L22 16 L16 22 C20 32 26 38 34 42 L40 36 L52 42 L50 50 C30 52 6 30 8 6 Z"/><rect x="30" y="6" width="34" height="22"/><path d="M30 6 L47 19 L64 6"/></svg>
    <span class="num">04</span>
    <h3>CONTACT US</h3>
    <p>Please contact us today with your requirements , this can be care workers</p>
  </div>

  <div class="abs display band-link" style="left:154px">UK Skilled<br>Workers List</div>
  <svg class="abs band-arrow" style="left:414px" width="32" height="32" viewBox="0 0 32 32" fill="none" stroke="#fff" stroke-width="2.5"><path d="M4 28 L28 4 M10 4 H28 V22"/></svg>
  <div class="abs display band-link" style="left:521px">Sponsor<br>Licence</div>
  <svg class="abs band-arrow" style="left:706px" width="32" height="32" viewBox="0 0 32 32" fill="none" stroke="#fff" stroke-width="2.5"><path d="M4 28 L28 4 M10 4 H28 V22"/></svg>
  <div class="abs display band-link" style="left:790px">Recruitment<br>Timeline</div>
  <svg class="abs band-arrow" style="left:999px" width="32" height="32" viewBox="0 0 32 32" fill="none" stroke="#fff" stroke-width="2.5"><path d="M4 28 L28 4 M10 4 H28 V22"/></svg>

  <!-- blog -->
  <h2 class="abs display blog-title">Read our<br>recent blog<br>articles</h2>
  <div class="abs see-all">SEE ALL ARTICLES
    <svg width="16" height="16" viewBox="0 0 16 16" fill="none" stroke="#d3112a" stroke-width="2"><path d="M2 14 L14 2 M5 2 H14 V11"/></svg>
  </div>
  <article class="abs post" style="left:575px">
    <div class="post-photo" role="img" aria-label="Hospitality staff team in chef whites and aprons" style="background:linear-gradient(180deg,#d9dde2 0%,#b9c2cc 60%,#8e7f6e 100%)"></div>
    <h4>UK HOSPITALITY INDUSTRY IN NEED OF WORKERS</h4>
    <div class="more">READ MORE</div>
  </article>
  <article class="abs post" style="left:894px">
    <div class="post-photo" role="img" aria-label="Farm worker holding a crate of fresh vegetables" style="background:linear-gradient(160deg,#5f7a3a 0%,#9a8a5a 45%,#c9563a 75%,#3f5a2a 100%)"></div>
    <h4>PUSH TO HIRE PHILIPPINE WORKERS FOR UK FARMS</h4>
    <div class="more">READ MORE</div>
  </article>

  <!-- map & footer -->
  <div class="abs footer"></div>
  <div class="abs map" role="img" aria-label="Greyscale map of the Philippines with office locations marked"></div>

  <div class="abs f-brand"><span class="brand-mark"></span><span class="brand-name">Brindle Staffing</span></div>
  <h3 class="abs display f-contact-title">Contact</h3>
  <div class="abs f-lines">
    <div><svg width="12" height="12" viewBox="0 0 12 12"><path d="M1 1 L4 0 L6 4 L4 5 C5 7 6 8 7 8 L8 6 L12 8 L11 11 C5 12 0 7 1 1 Z" fill="#d3112a"/></svg>07700 900418</div>
    <div><svg width="12" height="10" viewBox="0 0 12 10"><rect width="12" height="10" fill="#d3112a"/><path d="M0 0 L6 5 L12 0" fill="none" stroke="#000" stroke-width="1"/></svg>sales@brindlestaffing.example.com</div>
    <div><svg width="10" height="13" viewBox="0 0 10 13"><path d="M5 13 C5 13 0 7 0 5 A5 5 0 0 1 10 5 C10 7 5 13 5 13 Z" fill="#d3112a"/><circle cx="5" cy="5" r="2" fill="#000"/></svg>12 Orchard Row, Harbourton Harbourton<br>HX9 4 United Kingdom</div>
  </div>
  <span class="abs social" style="left:885px;background:#3b5bb0"></span>
  <span class="abs social" style="left:928px;background:#2aa3e8"></span>
  <span class="abs social" style="left:969px;background:#1b5f9e"></span>
  <span class="abs social" style="left:1010px;background:#c43a8a"></span>
  <div class="abs rule"></div>
  <div class="abs to-top"><svg width="12" height="8" viewBox="0 0 12 8" fill="none" stroke="#fff" stroke-width="2"><path d="M1 7 L6 2 L11 7"/></svg></div>
  <p class="abs copy">© 2023 All Rights Reserved | Brindle Staffing Ltd</p>
</div>
</body>
</html>
```